Business Card Design for Flood Rescue 360 - Property Restoration Professionals

I need a business card designed for Flood Rescue 360. We are a full-service property restoration solution. Providing water, fire, smoke & storm restoration as well as mold remediation and full remodel or reconstruction to homes and businesses across Dallas-Fort Worth, TX.
Target Market(s)
home and business owners with insurance covered property damage from water, fire or storm related damage
Industry/Entity Type
property restoration
Contact Information for Business Card
Marcus Pellow General Manager Cell: 214-555-0193 Office: 469-555-0148 email: Marcus@FloodRescue360.example services: Water, Fire, Mold, Reconstruction Tagline: Urgency for Your Water Emergency!
Look and feel
Each slider illustrates characteristics of the customer's brand and the style your logo design should communicate.

```html
<!DOCTYPE html>
<html lang="en">
<head>
<meta charset="utf-8">
<title>Flood Rescue 360 – Business Card</title>
<link href="https://fonts.googleapis.com/css2?family=Montserrat:wght@400;600;800&family=Lato:wght@400&display=swap" rel="stylesheet">
<style>
  :root{
    --bg:#262728;
    --card-white:#ffffff;
    --card-grey:#727272;
    --brand-blue:#00afe3;
    --ink-grey:#6b6b6b;
    --ink-dark:#555555;
  }
  *{box-sizing:border-box;margin:0;padding:0}
  html,body{width:1200px;height:952px;overflow:hidden;background:var(--bg)}
  .canvas{position:relative;width:1200px;height:952px}
  .card{position:absolute;left:340px;width:520px;height:298px;overflow:hidden;border-radius:2px;box-shadow:0 10px 30px rgba(0,0,0,.5)}
  .card-front{top:132px;background:var(--card-white)}
  .card-back{top:522px;background:var(--card-grey)}

  /* front */
  .person{position:absolute;left:40px;top:34px}
  .person-name{font-family:"Montserrat",sans-serif;font-size:24px;color:var(--brand-blue);letter-spacing:.5px;text-transform:uppercase;font-weight:400}
  .person-name strong{font-weight:800}
  .person-title{font-family:"Lato",sans-serif;font-size:14px;color:var(--ink-grey);margin-top:2px}
  .contacts{position:absolute;left:40px;top:102px;list-style:none}
  .contacts li{display:flex;align-items:center;gap:8px;font-family:"Lato",sans-serif;font-size:11.5px;color:var(--ink-dark);height:18px}
  .contacts svg{width:13px;height:13px;flex:none}
  .tagline{position:absolute;left:40px;top:168px;font-family:"Montserrat",sans-serif;font-weight:600;font-size:15px;line-height:19px;color:var(--ink-dark);text-transform:uppercase}
  .tagline em{font-style:normal;font-weight:800;color:var(--brand-blue)}
  .services{position:absolute;left:40px;top:214px;display:flex;gap:10px;list-style:none;font-family:"Lato",sans-serif;font-size:11.5px;color:var(--ink-dark)}
  .services li::before{content:"•";color:var(--brand-blue);margin-right:4px}
  .rule{position:absolute;left:0;top:244px;width:300px;height:2px;background:var(--brand-blue)}
  .rule-end{position:absolute;right:0;top:244px;width:40px;height:2px;background:var(--brand-blue)}
  .brand-front{position:absolute;left:316px;top:196px;display:flex;align-items:center;gap:8px}
  .brand-dot{width:22px;height:22px;border-radius:50%;background:var(--ink-grey);flex:none}
  .brand-front .brand-name{font-family:"Montserrat",sans-serif;font-weight:800;font-size:15px;color:var(--brand-blue);line-height:18px;text-transform:uppercase}

  /* back */
  .tab{position:absolute;background:var(--brand-blue);border-radius:6px}
  .tab-top{left:-8px;top:-8px;width:100px;height:30px}
  .tab-bottom{right:-8px;bottom:-8px;width:150px;height:48px}
  .brand-back{position:absolute;left:0;top:0;width:100%;height:100%;display:flex;align-items:center;justify-content:center;gap:16px}
  .brand-back .brand-name{font-family:"Montserrat",sans-serif;font-weight:800;font-size:34px;line-height:34px;color:#fff;text-transform:uppercase}
  .brand-ring{width:56px;height:56px;border-radius:50%;background:#fff;flex:none}
</style>
</head>
<body>
<main class="canvas">
  <section class="card card-front" aria-label="Business card front">
    <div class="person">
      <h1 class="person-name">Marcus <strong>Pellow</strong></h1>
      <p class="person-title">General Manager</p>
    </div>
    <ul class="contacts">
      <li><svg viewBox="0 0 16 16"><rect width="16" height="16" rx="3" fill="#6b6b6b"/><path d="M5 3.5l2 2-1 1.2c.6 1.3 1.5 2.2 2.8 2.8L10 8.5l2 2-1.2 1.8C7.5 12 4 8.5 3.7 5z" fill="#fff"/></svg>214-555-0193</li>
      <li><svg viewBox="0 0 16 16"><rect width="16" height="16" rx="3" fill="#6b6b6b"/><path d="M3 6.5c3-2.5 7-2.5 10 0l-1.5 1.5-2-1V6H6.5v1L4.5 8z" fill="#fff"/><rect x="4.5" y="8.5" width="7" height="4" rx="1" fill="#fff"/></svg>469-555-0148</li>
      <li><svg viewBox="0 0 16 16"><rect width="16" height="16" rx="3" fill="#6b6b6b"/><rect x="3" y="4.5" width="10" height="7" fill="#fff"/><path d="M3 4.5l5 4 5-4" fill="none" stroke="#6b6b6b" stroke-width="1"/></svg>marcus@floodrescue360.example</li>
    </ul>
    <p class="tagline">Urgency for<br>your <em>Water Emergency!</em></p>
    <ul class="services">
      <li>Water</li><li>Fire</li><li>Mold</li><li>Reconstruction</li>
    </ul>
    <div class="rule"></div>
    <div class="rule-end"></div>
    <div class="brand-front">
      <span class="brand-dot"></span>
      <span class="brand-name">Flood Rescue 360</span>
    </div>
  </section>

  <section class="card card-back" aria-label="Business card back">
    <div class="tab tab-top"></div>
    <div class="tab tab-bottom"></div>
    <div class="brand-back">
      <span class="brand-name">Flood<br>Rescue 360</span>
      <span class="brand-ring"></span>
    </div>
  </section>
</main>
</body>
</html>
```